New Company Newsletter Template Needed!!!

We need some new graphics/design for us to create our company newsletter in MS Publisher/Word. Prefer simple, modern design that can be easy to update each month, flexible for adding images and include our company logo (attached).
Also attached our basic existing template but we do not want to use the same “swoosh” ribbon and want to reduce the number of colours used.
Needs to be elements we can move into the software and create a PDF newsletter to circulate.

Font styles to use
Sans Serif

Requirements
Must have
• Company logo
Nice to have
• If any colours should fit into our company logo palette

```html
<!DOCTYPE html>
<html lang="en">
<head>
<meta charset="utf-8">
<title>Brightway Newsletter – January 2030</title>
<link href="https://fonts.googleapis.com/css2?family=Montserrat:ital,wght@0,400;0,500;0,600;0,700;0,800;1,700&display=swap" rel="stylesheet">
<style>
  :root {
    --crimson: #c8174f;
    --red: #e2403f;
    --orange: #f26b2a;
    --gold: #f7b500;
    --blue: #1c4fa5;
    --ink: #3a3a3a;
    --panel: #f3f5fb;
    --placeholder: #c4c5c8;
    --muted: #9a9a9a;
    --backdrop: #000;
  }
  * { box-sizing: border-box; margin: 0; padding: 0; }
  html, body { width: 1200px; height: 802px; overflow: hidden; background: var(--backdrop); }
  body { font-family: "Montserrat", sans-serif; color: var(--ink); position: relative; }

  .page { position: absolute; top: 14px; width: 577px; height: 768px; background: #fff; overflow: hidden; }
  .page--front { left: 18px; }
  .page--inside { left: 606px; }
  .swoosh { position: absolute; left: 0; width: 577px; display: block; }
  .swoosh--top { top: 0; }
  .swoosh--bottom { bottom: 0; }

  .brand { position: absolute; top: 22px; display: flex; align-items: center; gap: 7px; }
  .brand__dot { width: 30px; height: 30px; border-radius: 50%; background: var(--gold); }
  .brand__name { font-size: 26px; font-weight: 500; color: #fff; letter-spacing: -0.5px; line-height: 1; }
  .page--front .brand { right: 10px; }
  .page--inside .brand { left: 58px; }

  .masthead__title { position: absolute; left: 16px; top: 50px; font-size: 47px; font-weight: 800; color: #fff; letter-spacing: 0.5px; line-height: 1; }
  .masthead__meta { position: absolute; left: 16px; top: 107px; display: flex; gap: 24px; font-size: 10px; font-weight: 700; font-style: italic; color: #fff; }

  .sidebar { position: absolute; background: var(--panel); }
  .page--front .sidebar { left: 0; top: 230px; width: 225px; height: 538px; }
  .page--inside .sidebar { left: 352px; top: 90px; width: 225px; height: 678px; }

  .contents__banner { position: absolute; left: 0; top: 249px; width: 198px; height: 32px; background: var(--crimson); clip-path: polygon(0 0, 190px 0, 198px 32px, 0 32px); color: #fff; font-weight: 700; font-size: 16px; line-height: 32px; padding-left: 31px; }
  .contents__list { position: absolute; left: 35px; top: 288px; list-style: none; }
  .contents__list li { font-size: 14.5px; font-weight: 500; color: #444; height: 28.6px; line-height: 22px; }
  .contents__list li::before { content: "·"; margin-right: 7px; font-weight: 700; }

  .story { position: absolute; }
  .story p { font-size: 10.6px; line-height: 16.8px; margin-bottom: 16.8px; }
  .story--justified p { text-align: justify; hyphens: auto; }
  .headline { color: var(--blue); font-weight: 700; font-size: 28px; line-height: 1.1; letter-spacing: 0.2px; }
  .subhead { color: var(--crimson); font-weight: 700; font-size: 17px; line-height: 1.2; margin-bottom: 5px; }
  .side-text p { font-size: 10.6px; line-height: 15.7px; margin-bottom: 15.7px; }

  .lead { left: 246px; top: 262px; width: 322px; }
  .lead .headline { margin-bottom: 6px; }
  .sidebar-story { left: 20px; top: 491px; width: 194px; }
  .sideline { left: 375px; top: 110px; width: 192px; }

  .photo { position: absolute; background: var(--placeholder); display: flex; align-items: center; justify-content: center; color: #fff; font-weight: 500; font-size: 15px; letter-spacing: 0.5px; }
  .photo--main { left: 13px; top: 130px; width: 329px; height: 168px; font-size: 16px; }
  .photo--side { left: 368px; top: 523px; width: 200px; height: 125px; font-size: 12.5px; }

  .feature-title { position: absolute; left: 16px; top: 314px; }
  .column { top: 355px; width: 150px; }
  .column--first { left: 16px; }
  .column--second { left: 182px; }

  .copyright { position: absolute; right: 22px; bottom: 24px; color: var(--muted); font-size: 13px; letter-spacing: 0.3px; }
  .page--inside .copyright { right: 10px; bottom: 10px; }
</style>
</head>
<body>

<section class="page page--front">
  <svg class="swoosh swoosh--top" viewBox="0 0 577 240" height="240" aria-hidden="true">
    <defs>
      <linearGradient id="heatFront" x1="0" y1="0" x2="1" y2="0.4">
        <stop offset="0" stop-color="#d42d4e"/>
        <stop offset="0.55" stop-color="#e2403f"/>
        <stop offset="1" stop-color="#f26b2a"/>
      </linearGradient>
      <linearGradient id="berryFront" x1="0" y1="0" x2="1" y2="0">
        <stop offset="0" stop-color="#7d1236"/>
        <stop offset="0.5" stop-color="#c8174f"/>
        <stop offset="1" stop-color="#e2403f"/>
      </linearGradient>
    </defs>
    <path d="M0 0H577V110C480 150 330 236 170 232C90 230 30 200 0 184Z" fill="url(#berryFront)"/>
    <path d="M0 0H577V92C470 140 320 222 170 214C95 210 35 185 0 170Z" fill="#f7b500"/>
    <path d="M0 0H577V84C465 130 320 210 175 204C95 200 35 175 0 160Z" fill="url(#heatFront)"/>
  </svg>
  <div class="brand"><span class="brand__dot"></span><span class="brand__name">Brightway</span></div>
  <h1 class="masthead__title">NEWSLETTER</h1>
  <div class="masthead__meta"><span>January 2030</span><span>Issue #45</span><span>Company Important Info Goes here</span></div>

  <aside class="sidebar"></aside>
  <div class="contents__banner">Inside this Issue:</div>
  <ul class="contents__list">
    <li>Inside Story Title 2</li>
    <li>Inside Story Title 2</li>
    <li>Inside Story Title 3</li>
    <li>Inside Story Title 3</li>
    <li>Inside Story Title 4</li>
    <li>Inside Story Title 4</li>
  </ul>

  <article class="story side-text sidebar-story">
    <h3 class="subhead">Parragraph Title here</h3>
    <p>This story can fit 125-165 words. This is greeked text for copy placement. Use this as a placeholder for text when it's not readily available. This is a layout tool intended to aid in the design process, to provide adequate amounts of copy to proof a layout and style. It's a necessary element for building good design. Greeked copy is a standard in the marketing industry.</p>
  </article>

  <article class="story lead">
    <h2 class="headline">Lead Story Headline</h2>
    <p>This story can fit 125-165 words. This is greeked text for copy placement. Use this as a placeholder for text when it's not readily available. This is a layout tool intended to aid in the design process, to provide adequate amounts of copy to proof a layout and style. It's a necessary element for building good design. Greeked copy is a standard in the marketing industry.</p>
    <p>The process of This story can fit 125-165 words. This is greeked text for copy placement. Use this as a placeholder for text when it's not readily available. This is a layout tool intended to aid in the design process, to provide adequate amounts of copy to proof a layout and style. It's a necessary element for building good design. Greeked copy is a standard in the marketing industry.</p>
    <p>The process of This story can fit 125-165 words. This is greeked text for copy placement. Use this as a placeholder for text when it's not readily available. This is a layout tool intended to aid in the design process, to provide adequate amounts of copy to proof a layout and style.</p>
  </article>

  <svg class="swoosh swoosh--bottom" viewBox="0 0 577 120" height="120" aria-hidden="true">
    <path d="M0 84C170 60 380 0 577 10V40C400 30 230 90 90 120H0Z" fill="#f7b500"/>
    <path d="M0 74C170 50 380 -8 577 2V30C400 22 220 84 60 120H0Z" fill="url(#berryFront)"/>
  </svg>
  <div class="copyright">Copyright text here</div>
</section>

<section class="page page--inside">
  <svg class="swoosh swoosh--top" viewBox="0 0 577 110" height="110" aria-hidden="true">
    <defs>
      <linearGradient id="heatInside" x1="0" y1="0" x2="1" y2="0">
        <stop offset="0" stop-color="#c8174f"/>
        <stop offset="0.6" stop-color="#e2403f"/>
        <stop offset="1" stop-color="#f26b2a"/>
      </linearGradient>
    </defs>
    <path d="M0 0H577V40C470 55 320 105 170 94C100 90 40 80 0 72Z" fill="url(#heatInside)"/>
    <path d="M0 0H577V16C450 34 300 92 160 80C95 74 40 64 0 58Z" fill="#f7b500"/>
    <path d="M0 0H577V8C450 26 300 82 165 70C95 64 40 54 0 50Z" fill="url(#heatInside)"/>
  </svg>
  <div class="brand"><span class="brand__dot"></span><span class="brand__name">Brightway</span></div>

  <aside class="sidebar"></aside>

  <div class="photo photo--main" role="img" aria-label="Feature photograph placeholder">IMAGE HERE</div>
  <h2 class="headline feature-title">Main Image Title here</h2>
  <article class="story story--justified column column--first">
    <p>This story can fit 125-165 words. This is greeked text for copy placement. Use this as a placeholder for text when it's not readily available. This is a layout tool intended to aid in the design process, to provide adequate amounts of copy to proof a layout and style. It's a necessary element for building good design. Greeked copy is a standard in the marketing industry.</p>
    <p>The process of This story can fit 125-165 words. This is greeked text for copy placement. Use this as a placeholder for text when it's not readily available.</p>
  </article>
  <article class="story story--justified column column--second">
    <p>This story can fit 125-165 words. This is greeked text for copy placement. Use this as a placeholder for text when it's not readily available. This is a layout tool intended to aid in the design process, to provide adequate amounts of copy to proof a layout and style. It's a necessary element for building good design. Greeked copy is a standard in the marketing industry.</p>
    <p>The process of This story can fit 125-165 words. This is greeked text for copy placement.</p>
  </article>

  <article class="story side-text sideline">
    <h3 class="subhead">Side Bard Content</h3>
    <p>This story can fit 125-165 words. This is greeked text for copy placement. Use this as a placeholder for text when it's not readily available. This is a layout tool intended to aid in the design process, to provide adequate amounts of copy to proof a layout and style. It's a necessary element for building good design. Greeked copy is a standard in the marketing industry.</p>
    <p>The process of This story can fit 125-165 words. This is greeked text for copy placement. Use this as a placeholder for text when it's not readily available. This is a layout tool intended to aid in the design process, to provide adequate amounts of copy to proof a layout and style. It's a necessary element for building good design. Greeked copy is a standard in the marketing industry.</p>
  </article>
  <div class="photo photo--side" role="img" aria-label="Sidebar photograph placeholder">IMAGE HERE</div>

  <svg class="swoosh swoosh--bottom" viewBox="0 0 577 90" height="90" aria-hidden="true">
    <path d="M0 80C200 50 420 0 577 20V44C420 30 250 70 120 90H0Z" fill="#f7b500"/>
    <path d="M0 68C200 40 420 -8 577 12V34C420 24 240 66 90 90H0Z" fill="url(#heatInside)"/>
  </svg>
  <div class="copyright">Copyright text here</div>
</section>

</body>
</html>
```